- Redesign our business card
- Logo remains unchanged
- Current business card attached

Target Market(s)

We are a property management company

Industry/Entity Type

Business

```html
<!DOCTYPE html>
<html lang="en">
<head>
<meta charset="utf-8">
<title>Harlow Property Group – Business Card</title>
<link rel="stylesheet" href="https://fonts.googleapis.com/css2?family=Arimo:ital,wght@0,400;0,700;1,400;1,700&family=Tinos&display=swap">
<style>
  :root {
    --sand: #dcd3b2;
    --olive: #7d7c43;
    --slate: #6d6e71;
    --ink: #5f6062;
    --edge: #c9c9c9;
    --paper: #ffffff;
  }
  * { margin: 0; padding: 0; box-sizing: border-box; }
  html, body { width: 1200px; height: 900px; overflow: hidden; background: var(--paper); }
  .stage { position: relative; width: 1200px; height: 900px; font-family: "Arimo", Arial, sans-serif; color: var(--ink); }

  .card { position: absolute; background: var(--paper); border: 1px solid var(--edge); box-shadow: 0 1px 3px rgba(0,0,0,.12); overflow: hidden; }
  .card--front { left: 78px; top: 330px; width: 476px; height: 304px; }
  .card--back { left: 628px; top: 334px; width: 484px; height: 306px; }

  .side-label { position: absolute; top: 670px; font-family: "Tinos", "Times New Roman", serif; font-size: 56px; color: #111; transform: translateX(-50%); }
  .side-label--front { left: 306px; }
  .side-label--back { left: 854px; }

  /* front */
  .brand { position: absolute; left: 156px; top: 72px; }
  .brand__mark { width: 80px; height: 80px; background: var(--sand); margin-left: 20px; margin-bottom: 8px; }
  .brand__name { font-weight: 700; font-size: 15px; color: var(--olive); letter-spacing: .2px; white-space: nowrap; }
  .brand__tagline { font-size: 9px; color: var(--slate); letter-spacing: .6px; text-transform: uppercase; margin-top: 2px; border-top: 1px solid var(--slate); padding-top: 2px; width: 200px; white-space: nowrap; }

  .services { position: absolute; left: 28px; top: 210px; font-size: 12px; color: var(--ink); display: flex; gap: 6px; align-items: center; white-space: nowrap; }
  .services__arrow { width: 10px; height: 8px; }
  .website { position: absolute; left: 158px; top: 238px; font-size: 11px; font-weight: 700; color: var(--ink); }

  .bands { position: absolute; display: flex; gap: 8px; }
  .bands--front { left: 0; right: 0; bottom: 2px; height: 28px; }
  .bands--back { left: 0; right: 0; top: 6px; height: 22px; }
  .band { flex: 1; }
  .band--sand { background: var(--sand); }
  .band--olive { background: var(--olive); }
  .band--slate { background: var(--slate); }

  /* back */
  .person { position: absolute; left: 14px; top: 182px; }
  .person__name { font-style: italic; font-weight: 700; font-size: 12px; color: var(--olive); }
  .person__role { font-size: 12px; color: var(--olive); margin-top: 3px; }
  .person__rule { position: absolute; left: 0; top: 220px; width: 134px; height: 2px; background: var(--slate); }
  .contact { position: absolute; left: 14px; top: 236px; font-size: 11px; line-height: 16px; color: var(--ink); font-style: normal; }
  .back-mark { position: absolute; right: 14px; top: 198px; display: flex; flex-direction: column; align-items: center; gap: 6px; }
  .back-mark__square { width: 60px; height: 60px; background: var(--sand); }
  .back-mark__name { font-weight: 700; font-size: 9px; color: var(--olive); white-space: nowrap; }
</style>
</head>
<body>
<main class="stage">
  <section class="card card--front" aria-label="Card front">
    <div class="brand">
      <div class="brand__mark"></div>
      <div class="brand__name">HARLOW PROPERTY GROUP</div>
      <div class="brand__tagline">Strata Management Services</div>
    </div>
    <p class="services">
      <span>Strata Management</span>
      <svg class="services__arrow" viewBox="0 0 10 8"><path d="M0 2h5V0l5 4-5 4V6H0z" fill="#7d7c43"/></svg>
      <span>Community Management</span>
      <svg class="services__arrow" viewBox="0 0 10 8"><path d="M0 2h5V0l5 4-5 4V6H0z" fill="#7d7c43"/></svg>
      <span>Property Management</span>
    </p>
    <p class="website">www.harlowproperty.com.au</p>
    <div class="bands bands--front">
      <div class="band band--sand"></div>
      <div class="band band--olive"></div>
      <div class="band band--slate"></div>
    </div>
  </section>
  <div class="side-label side-label--front">front</div>

  <section class="card card--back" aria-label="Card back">
    <div class="bands bands--back">
      <div class="band band--sand"></div>
      <div class="band band--olive"></div>
      <div class="band band--slate"></div>
    </div>
    <div class="person">
      <p class="person__name">Daniel Harlow</p>
      <p class="person__role">Licensed Strata Manager</p>
    </div>
    <div class="person__rule"></div>
    <address class="contact">
      Po Box 18, Harbour Hills Nsw 2012<br>
      12/6-20 Linden Street Eastvale Nsw 2010<br>
      <strong>T: 02 5550 1840</strong> F: 02 5550 1841 M: 0400 555 017<br>
      E: info@harlowproperty.com.au - www.harlowproperty.com.au
    </address>
    <div class="back-mark">
      <div class="back-mark__square"></div>
      <div class="back-mark__name">HARLOW PROPERTY GROUP</div>
    </div>
  </section>
  <div class="side-label side-label--back">back</div>
</main>
</body>
</html>
```